Letterhead for SaaS

Design a letterhead that aligns with our new business card, using our logo and color scheme and text defined in the Branding Guide to ensure consistency. Consider incorporating a subtle watermark for added elegance. The layout should reflect the card's style, creating a cohesive look across our stationery.

```html
<!DOCTYPE html>
<html lang="en">
<head>
<meta charset="utf-8">
<title>Vornex Letterhead</title>
<link rel="stylesheet" href="https://fonts.googleapis.com/css2?family=Arimo:wght@400;700&display=swap">
<style>
  :root {
    --paper: #f6f4f4;
    --ink: #4a4a4a;
    --ink-dark: #121a26;
    --accent: #00c0f3;
    --white: #ffffff;
  }
  * { box-sizing: border-box; margin: 0; padding: 0; }
  html, body { width: 942px; height: 1200px; overflow: hidden; }
  body { background: var(--paper); font-family: "Arimo", Helvetica, Arial, sans-serif; color: var(--ink); }
  .letterhead { position: relative; width: 942px; height: 1200px; background: var(--paper); }

  .brand { position: absolute; left: 65px; top: 60px; }
  .brand-square { width: 64px; height: 64px; background: var(--ink-dark); margin-left: 30px; }
  .brand-name { margin-top: 52px; font-size: 23px; font-weight: 700; color: var(--ink-dark); letter-spacing: 0.5px; }

  .contact { position: absolute; right: 59px; top: 103px; font-size: 14px; color: var(--ink-dark); line-height: 19px; }
  .contact-line { display: flex; align-items: center; gap: 7px; }
  .contact-icon { width: 12px; height: 12px; fill: var(--ink-dark); }

  .salutation { position: absolute; left: 65px; top: 296px; font-size: 25px; font-weight: 400; color: var(--ink); }

  .body-copy { position: absolute; left: 65px; top: 370px; width: 818px; font-size: 13.4px; line-height: 19.8px; text-align: justify; color: var(--ink); }
  .body-copy p + p { margin-top: 19.8px; }

  .closing { position: absolute; left: 65px; top: 796px; font-size: 13.4px; }
  .signature { position: absolute; left: 76px; top: 874px; width: 124px; height: 46px; background: linear-gradient(180deg, rgba(18,26,38,0.08), rgba(18,26,38,0.18)); }
  .signer { position: absolute; left: 76px; top: 940px; }
  .signer-name { font-size: 19px; color: var(--ink); }
  .signer-role { font-size: 15px; margin-top: 4px; color: var(--ink); }

  .footer { position: absolute; left: 0; bottom: 0; width: 942px; height: 66px; }
  .footer svg { display: block; width: 100%; height: 100%; }
  .footer-url { position: absolute; right: 59px; bottom: 14px; font-size: 14px; letter-spacing: 3px; color: var(--white); }
</style>
</head>
<body>
<main class="letterhead">
  <header class="brand">
    <div class="brand-square"></div>
    <div class="brand-name">VORNEX</div>
  </header>

  <address class="contact" style="font-style: normal;">
    <div class="contact-line">
      <svg class="contact-icon" viewBox="0 0 24 24"><path d="M6.6 10.8a15.1 15.1 0 0 0 6.6 6.6l2.2-2.2c.3-.3.7-.4 1-.2 1.1.4 2.3.6 3.6.6.6 0 1 .4 1 1V20c0 .6-.4 1-1 1A17 17 0 0 1 3 4c0-.6.4-1 1-1h3.5c.6 0 1 .4 1 1 0 1.3.2 2.5.6 3.6.1.3 0 .7-.2 1z"/></svg>
      <span>(555) 014-2290</span>
    </div>
    <div class="contact-line">
      <svg class="contact-icon" viewBox="0 0 24 24"><path d="M2 5h20v14H2z M2 5l10 8 10-8" fill="var(--ink-dark)"/><path d="M3 6l9 7 9-7" stroke="var(--paper)" stroke-width="1.6" fill="none"/></svg>
      <span>mara.l@vornex.com</span>
    </div>
  </address>

  <h1 class="salutation">Dear Mr. Dalton,</h1>

  <section class="body-copy">
    <p>Lorem ipsum dolor sit amet, consectetur adipiscing elit. Donec orci purus, luctus vitae dignissim eu, iaculis sed purus. Vivamus faucibus, ipsum nec aliquet viverra, leo mauris condimentum ligula, sit amet sagittis enim ligula quis arcu. Nam egestas tortor id nisi porttitor mattis. In tortor ante, ultricies in suscipit a, tempus non massa. Vivamus et auctor mi. Fusce vel massa nulla. Phasellus nec eros mauris, et scelerisque orci.</p>
    <p>Donec malesuada orci vitae nulla accumsan porta a id massa. Quisque accumsan iaculis magna sit amet fringilla. Maecenas consequat, magna eget tincidunt semper, odio nibh rutrum mi, id feugiat ante nisi eu risus. Vestibulum nunc orci, rhoncus a placerat in, ultricies in mi. Cras mattis varius eros, vel fringilla nisi suscipit eget. Quisque scelerisque sagittis nulla at porttitor.</p>
    <p>Sed id augue vitae urna euismod commodo aliquet a quam. Pellentesque arcu velit, cursus et malesuada ut, consequat et diam. Nullam erat sem, rhoncus id ullamcorper vitae, rhoncus et arcu. In ultricies ultricies nulla, ut rutrum nisi iaculis at. Donec eu magna a metus ornare faucibus. Fusce aliquet faucibus ultricies. Morbi semper, est id tincidunt gravida, sem arcu adipiscing lacus, ac bibendum nulla leo eu purus. Quisque nec diam sed risus consectetur a ccumsan quis quis nibh. Vestibulum id purus lorem.</p>
    <p>It is a long established fact that a reader will be distracted by the readable content of a page when looking at its layout. The point of using Lorem Ipsum is that it has a more-or-less normal distribution of letters, as opposed to using 'Content here, content here', making it look like readable English. Many desktop publishing packages</p>
  </section>

  <p class="closing">Sincerely,</p>
  <div class="signature" role="img" aria-label="Handwritten signature of Peter Hale"></div>
  <div class="signer">
    <div class="signer-name">Peter Hale</div>
    <div class="signer-role">CEO/ Founder</div>
  </div>

  <footer class="footer">
    <svg viewBox="0 0 942 66" preserveAspectRatio="none">
      <rect x="0" y="0" width="942" height="66" fill="var(--accent)"/>
      <polygon points="0,66 942,2 942,66" fill="var(--ink-dark)"/>
      <line x1="0" y1="65" x2="942" y2="1" stroke="var(--white)" stroke-width="2.5"/>
    </svg>
    <span class="footer-url">www.vornex.com</span>
  </footer>
</main>
</body>
</html>
```